Stationery Design needed for logo design project

This project is linked to Pediatric Therapy Clinic for children with autism and other special needs needs new logo design.

Our company needs a Stationery Design. Please refer to our original project in the link above.

Reason: Too much to do right now while enjoying Christmas with all my family!

```html
<!DOCTYPE html>
<html lang="en">
<head>
<meta charset="utf-8">
<title>Kindred Steps Stationery</title>
<link href="https://fonts.googleapis.com/css2?family=Open+Sans:wght@400;600;700;800&display=swap" rel="stylesheet">
<style>
:root{
  --backdrop:#ececec;
  --paper:#ffffff;
  --teal:#3cbfcb;
  --brand:#1fa3d6;
  --accent:#e8452b;
  --ink:#3a3a3a;
  --ink-soft:#6b6b6b;
  --sig:#dcdcdc;
}
*{box-sizing:border-box;margin:0;padding:0}
html,body{width:1200px;height:937px;overflow:hidden}
body{background:var(--backdrop);font-family:"Open Sans",Arial,sans-serif;color:var(--ink);position:relative}
.sheet{position:absolute;background:var(--paper);box-shadow:0 2px 6px rgba(0,0,0,.12)}

.brand-name{display:flex;align-items:center;gap:5px;font-weight:800;color:var(--brand);white-space:nowrap}
.brand-dot{border-radius:50%;background:var(--brand);flex:none}

/* letterhead */
.letterhead{left:185px;top:66px;width:388px;height:546px}
.letterhead .brand-name{position:absolute;left:20px;top:38px;font-size:17px}
.letterhead .brand-dot{width:11px;height:11px}
.letter-contact{position:absolute;right:20px;top:23px;text-align:right;font-size:5px;line-height:7.5px;color:var(--ink-soft);font-style:normal}
.letter-body{position:absolute;left:36px;top:139px;width:296px;font-size:5.3px;line-height:9px;color:var(--ink-soft)}
.letter-body p{margin:0}
.letter-body .date{margin-bottom:3px}
.letter-body .greeting{color:var(--ink);font-weight:700}
.letter-body .para-1{margin-bottom:14px}
.letter-body .para-2{margin-bottom:25px}
.letter-body .para-3{margin-bottom:11px}
.signature{width:30px;height:22px;background:var(--sig);margin:8px 0 8px}
.signer{color:var(--ink);font-weight:700}
.letter-body .role{margin-bottom:3px}

/* folder */
.folder{left:636px;top:40px;width:458px;height:576px;display:flex;align-items:center;justify-content:center}
.folder .brand-name{font-size:44px;gap:12px;margin-top:-20px}
.folder .brand-dot{width:26px;height:26px}

/* business cards */
.card-front{left:46px;top:658px;width:176px;height:100px}
.card-front .brand-name{position:absolute;left:10px;top:20px;font-size:10px;gap:3px}
.card-front .brand-dot{width:6px;height:6px}
.card-person{position:absolute;right:8px;top:52px;text-align:right}
.card-person .name{font-size:7px;font-weight:700;color:var(--accent)}
.card-person .role{font-size:5.5px;color:var(--ink-soft)}
.card-contact{position:absolute;left:8px;bottom:8px;font-size:3.6px;line-height:5px;color:var(--ink-soft)}
.card-contact span{color:var(--accent)}
.card-web{position:absolute;right:8px;bottom:8px;font-size:4.2px;letter-spacing:1px;color:var(--accent)}
.card-back{left:46px;top:785px;width:176px;height:100px;background:var(--teal);display:flex;align-items:center;justify-content:center}
.card-back .web{color:#fff;font-size:7px;letter-spacing:1.4px}

/* envelopes */
.envelope-front{left:265px;top:672px;width:432px;height:208px}
.envelope-front .brand-name{position:absolute;left:18px;top:52px;font-size:15px}
.envelope-front .brand-dot{width:10px;height:10px}
.envelope-address{position:absolute;left:18px;top:104px;font-size:4.6px;font-weight:700;color:var(--ink)}
.envelope-back{left:737px;top:672px;width:432px;height:208px;overflow:hidden}
.envelope-flap{position:absolute;left:0;top:0;width:100%;height:72px;background:var(--teal);border-radius:0 0 36px 58px}
.envelope-flap .web{position:absolute;left:0;right:0;top:28px;text-align:center;color:#fff;font-size:9px;letter-spacing:2.4px}
</style>
</head>
<body>

<section class="sheet letterhead">
  <div class="brand-name"><span class="brand-dot"></span>Kindred Steps</div>
  <address class="letter-contact">
    1420 Maple Crest Rd<br>Austin TX 78701<br>512.555.0142<br>mara@kindredsteps.com
  </address>
  <div class="letter-body">
    <p class="date">July 2, 2012</p>
    <p class="greeting">Dear CH,</p>
    <p>ABC Building, def St., Country Name</p>
    <p class="para-1">Thank you for choosing our clinic for your child's therapy. Our team of licensed therapists works closely with each family to build a care plan that fits daily routines at home and at school. We focus on play based sessions that encourage communication, movement and confidence, and we share progress notes after every visit so parents always know what comes next. Each plan is reviewed every month with the family, and goals are adjusted as your child grows. We also offer evening times for working parents and a quiet waiting room for siblings.</p>
    <p class="para-2">Please call our front desk if you would like to schedule an evaluation or ask about available session times for the coming season.</p>
    <p class="para-3">Our sessions include speech, occupational and physical therapy, along with parent coaching and small group programs. We welcome questions at any time and look forward to supporting your family as your child grows, learns and reaches new goals at home, at school and in the community. Our staff can also help with insurance forms, school meetings and referrals to local partners. Every family receives a welcome folder with schedules, contact numbers and simple activities to continue practice between visits.</p>
    <p>Best Regards,</p>
    <div class="signature" role="img" aria-label="Handwritten signature"></div>
    <p class="signer">Daniel Reyes</p>
    <p class="role">Director</p>
    <p>ABC Building, def St., Country Name</p>
  </div>
</section>

<section class="sheet folder">
  <div class="brand-name"><span class="brand-dot"></span>Kindred Steps</div>
</section>

<section class="sheet card-front">
  <div class="brand-name"><span class="brand-dot"></span>Kindred Steps</div>
  <div class="card-person">
    <div class="name">Mara Ellison</div>
    <div class="role">Owner</div>
  </div>
  <div class="card-contact">
    <span>&#9679;</span> 512.555.0142<br>
    <span>&#9679;</span> mara@kindredsteps.com<br>
    <span>&#9679;</span> 1420 Maple Crest Rd, Austin TX 78701
  </div>
  <div class="card-web">www.kindredsteps.com</div>
</section>

<section class="sheet card-back">
  <div class="web">www.<b>kindredsteps</b>.com</div>
</section>

<section class="sheet envelope-front">
  <div class="brand-name"><span class="brand-dot"></span>Kindred Steps</div>
  <div class="envelope-address">1420 Maple Crest Rd, Austin TX 78701</div>
</section>

<section class="sheet envelope-back">
  <div class="envelope-flap">
    <div class="web">www.<b>kindredsteps</b>.com</div>
  </div>
</section>

</body>
</html>
```